ko7ara card

the business is a virtual space for showcasing art, libraries, science, food and gifts

high end - new look - nothing fussy - clean lines - bit of colour

needs to last for ten years - at least

think the number 11 in yellow with a purple background

hope that is enough of a brief - smile

Target Market(s)

all ages

Industry/Entity Type

Business

Contact Information for Business Card

ko7ara.com
tam corley = caretaker
virtual space & larkdale qn > norlandia

Requirements
Must have
• happy for you to choose
Nice to have
• ditto
Should not have
• anything boring - something that appeals to Gen I

```html
<!DOCTYPE html>
<html lang="en">
<head>
<meta charset="utf-8">
<title>ko7ara card</title>
<link rel="stylesheet" href="https://fonts.googleapis.com/css2?family=Exo+2:wght@700&family=Open+Sans:wght@400&display=swap">
<style>
  :root {
    --stage: #e9e9e9;
    --violet-deep: #4b2a9c;
    --violet: #6a3fc0;
    --indigo: #3b46b5;
    --magenta: #9c1f8a;
    --yellow: #f2e51a;
    --pink: #e9a3c9;
    --pink-text: #f6c3df;
    --frame: #141414;
    --mat: #ffffff;
  }
  * { margin: 0; padding: 0; box-sizing: border-box; }
  html, body { width: 1200px; height: 1200px; overflow: hidden; }
  body {
    background: var(--stage);
    display: flex;
    flex-direction: column;
    align-items: center;
    justify-content: center;
    gap: 80px;
  }
  .card {
    position: relative;
    width: 600px;
    height: 343px;
    overflow: hidden;
    box-shadow: 0 10px 30px rgba(0,0,0,0.15);
  }

  /* Front */
  .card-front {
    background:
      radial-gradient(circle at 20% 25%, rgba(120,80,210,0.7), transparent 45%),
      radial-gradient(circle at 80% 80%, rgba(60,70,190,0.7), transparent 50%),
      linear-gradient(135deg, var(--violet) 0%, var(--violet-deep) 50%, var(--indigo) 100%);
  }
  .front-band {
    position: absolute;
    left: 0; right: 0;
    top: 120px;
    height: 90px;
    background: var(--magenta);
  }
  .gallery-row {
    position: absolute;
    top: 55px;
    left: 0; right: 0;
    display: flex;
    justify-content: center;
    align-items: center;
    gap: 26px;
  }
  .artwork-frame { background: var(--frame); padding: 6px; }
  .artwork-mat { background: var(--mat); padding: 8px; }
  .artwork { display: block; }
  .artwork-figures { width: 100px; height: 140px; background: linear-gradient(160deg, #e9c48a, #c8553a 60%, #8a2a22); }
  .artwork-nebula  { width: 110px; height: 112px; background: radial-gradient(circle, #7aa6e0 15%, #d86a2a 35%, #2a1510 60%, #000 80%); }
  .artwork-stained { width: 100px; height: 140px; background: linear-gradient(150deg, #2f8c6a, #d8b63a 35%, #c23a2e 60%, #2b4fa6); }
  .brand-name {
    position: absolute;
    left: 0; right: 0;
    top: 240px;
    text-align: center;
    font-family: "Exo 2", sans-serif;
    font-weight: 700;
    font-size: 58px;
    color: var(--yellow);
    letter-spacing: 1px;
  }

  /* Back */
  .card-back { background: var(--pink); }
  .back-artwork {
    position: absolute;
    left: 0; top: 0; bottom: 0;
    width: 300px;
    background: linear-gradient(180deg, #f3c63a 0%, #e2652e 32%, #b45a3a 48%, #2e7fc2 62%, #1f4f9a 100%);
  }
  .back-band {
    position: absolute;
    left: 0; right: 0;
    top: 78px;
    height: 96px;
    background: var(--magenta);
    padding: 14px 22px;
    font-family: "Open Sans", sans-serif;
    font-size: 20px;
    line-height: 1.3;
    color: var(--pink-text);
  }
  .contact-line { display: block; white-space: nowrap; }
  .contact-line.indent { padding-left: 262px; }
</style>
</head>
<body>
  <section class="card card-front">
    <div class="front-band"></div>
    <div class="gallery-row">
      <div class="artwork-frame"><div class="artwork-mat"><span class="artwork artwork-figures" role="img" aria-label="Painting of colourful figures"></span></div></div>
      <div class="artwork-frame"><div class="artwork-mat"><span class="artwork artwork-nebula" role="img" aria-label="Photograph of a nebula"></span></div></div>
      <div class="artwork-frame"><div class="artwork-mat"><span class="artwork artwork-stained" role="img" aria-label="Stained-glass style artwork"></span></div></div>
    </div>
    <div class="brand-name">ko7ara.com</div>
  </section>

  <section class="card card-back">
    <div class="back-artwork" role="img" aria-label="Painted illustration of flames over swirling blue waves"></div>
    <div class="back-band">
      <span class="contact-line">ko7ara.com tam corley = &nbsp;caretaker virtual space &amp;</span>
      <span class="contact-line indent">larkdale qn &gt; norlandia</span>
    </div>
  </section>
</body>
</html>
```